Brindlequest.com is a mountain biking and climbing travel company. We need a advertisement fo...

We need a advertisement for the back cover of a guide book. We would like a simple but strong ad that includes our logo. It must state that we are a biking and climbing company and people can contact us at the web site brindlequest.com We would like you to incorparate and below photo and logo on the ad.

```html
<!DOCTYPE html>
<html lang="en">
<head>
<meta charset="utf-8">
<title>Brindlequest – back cover advertisement</title>
<link rel="stylesheet" href="https://fonts.googleapis.com/css2?family=Poppins:wght@300;500;600&display=swap">
<style>
  :root {
    --backdrop: #f3e6cf;
    --ink-light: #ffffff;
    --accent: #f2a21a;
    --shade: #120d0a;
    --wall-warm: #c9a57a;
    --wall-cream: #e6dccb;
    --hill-green: #3f5a33;
    --street-grey: #7d7873;
    --lamp-glow: #e39a3c;
  }
  html, body {
    margin: 0;
    width: 1200px;
    height: 1200px;
    overflow: hidden;
    background: var(--backdrop);
    font-family: "Poppins", sans-serif;
  }
  .cover {
    position: absolute;
    left: 200px;
    top: 30px;
    width: 800px;
    height: 1140px;
    overflow: hidden;
    background: var(--shade);
  }
  .cover__photo {
    position: absolute;
    inset: 0;
    background:
      radial-gradient(ellipse 30% 18% at 50% 50%, rgba(227,154,60,.75), transparent 70%),
      linear-gradient(90deg, var(--wall-warm) 0%, #b98a6c 22%, transparent 40%, transparent 60%, var(--wall-cream) 75%, #d8cbb6 100%),
      linear-gradient(180deg, #6c7f8f 0%, var(--hill-green) 12%, #4b5a3c 34%, var(--lamp-glow) 50%, var(--street-grey) 64%, #5b5652 100%);
  }
  .cover__fade {
    position: absolute;
    left: 0; right: 0; bottom: 0;
    height: 48%;
    background: linear-gradient(180deg, rgba(18,13,10,0) 0%, rgba(40,28,20,.75) 40%, var(--shade) 100%);
  }
  .brand {
    position: absolute;
    top: 270px;
    left: 0; right: 0;
    display: flex;
    flex-direction: column;
    align-items: center;
    gap: 6px;
  }
  .brand__mark {
    display: flex;
    align-items: center;
    gap: 16px;
  }
  .brand__dot {
    width: 30px;
    height: 30px;
    border-radius: 50%;
    background: var(--ink-light);
  }
  .brand__name {
    font-weight: 600;
    font-size: 52px;
    line-height: 1.1;
    letter-spacing: 1px;
    color: var(--ink-light);
  }
  .brand__services {
    margin: 0;
    padding-left: 46px;
    font-weight: 500;
    font-size: 17px;
    letter-spacing: 9px;
    text-transform: uppercase;
    color: var(--ink-light);
  }
  .message {
    position: absolute;
    left: 0; right: 0;
    bottom: 120px;
    text-align: center;
  }
  .message__tagline {
    margin: 0;
    font-weight: 300;
    font-size: 50px;
    line-height: 1.15;
    color: var(--ink-light);
  }
  .message__url {
    display: block;
    margin-top: 18px;
    font-weight: 500;
    font-size: 40px;
    color: var(--accent);
    text-decoration: none;
  }
</style>
</head>
<body>
  <main class="cover">
    <div class="cover__photo" role="img" aria-label="Evening photo of a narrow cobbled Italian street lined with old pastel buildings, lit shopfronts and a wooded hill beyond, with a cyclist riding past in motion blur"></div>
    <div class="cover__fade"></div>
    <div class="brand">
      <div class="brand__mark">
        <span class="brand__dot"></span>
        <span class="brand__name">Brindlequest</span>
      </div>
      <p class="brand__services">climbing + riding</p>
    </div>
    <div class="message">
      <p class="message__tagline">adventure cycle tours<br>… without the stress</p>
      <a class="message__url" href="#">brindlequest.com</a>
    </div>
  </main>
</body>
</html>
```